Website Design for new skincare product launch/rebranding

The Dew Harbor website is currently live and built through Pagelume.com. While the existing site has served as a strong starting point, I’m now looking to elevate the overall experience with a complete redesign that reflects the growth and vision of the brand. This will be a full visual and functional revamp — not just a refresh — with the goal of creating a more elevated, intuitive, and conversion-focused platform. I’m looking for a designer who can not only reimagine the layout and visuals, but also collaborate on optimizing the user journey and site structure for both storytelling and sales.

Target Market(s)

Age 25- 45 (core), with secondary appeal to 18-55. Primarily women, but gender inclusive. Wellness/Holistic Beauty/Organic Ingredients, Botanical.

Industry/Entity Type

Beauty, aesthetics, wellness.

Number of Pages Required

5+ page

Font styles to use
Other font styles liked:
• Thorvale Sans Family

Colors

Designer to choose colors to be used in the design.

Requirements
Must have
• Include standard pages (Home, Our Story/Values, Shop, Product Detail with ingredients/description/etc., Contact) and any other recommended sections to optimize conversion. Minimal, clean, calming visual. Seamlessly integrate with Vendara for all product sales.
Nice to have
• Company colors are attached in images, along with first two products that are launching. One called Lumivelt, and one called Serapoise. Fonts and shapes need to align accordingly. Feel elevated, neutral, and luxe while maintaining a grounded, earthy minimalism. Visual inspiration includes brands like Maple Tenet, Vessa Orlaine, and TOrveli — minimal yet high-end, with thoughtful use of whitespace, typography, and subtle movement. Would LOVE to have movement (short clip GIF) on either the home page or ingredient page, reference TOrveli website (homepage or LumaKnit Process™ Tab)
Should not have
• dark colors, complex design elements, too many different fonts. For ingredients, stick to botanical images and information only, with no mentions of CBD or use of leaf imagery.

```html
<!DOCTYPE html>
<html lang="en">
<head>
<meta charset="utf-8">
<title>Dew Harbor — Elevated Skin Wellness</title>
<link href="https://fonts.googleapis.com/css2?family=Libre+Baskerville:wght@400;700&family=Poppins:wght@300;400;500&display=swap" rel="stylesheet">
<style>
:root{
  --ink:#1c1b1a;
  --heading:#8b8785;
  --muted:#9a9492;
  --blush:#d8c3bc;
  --blush-soft:#ece2de;
  --hero:#e7dcd8;
  --paper:#ffffff;
  --shell:#faf5f3;
  --field:#f3efee;
  --footer:#a9a7a1;
  --line:#e6e1df;
  --star:#e9a23b;
}
*{box-sizing:border-box;margin:0;padding:0}
html,body{width:1200px;height:4454px;overflow:hidden}
body{position:relative;background:var(--paper);font-family:"Libre Baskerville",Georgia,serif;color:var(--muted)}
.abs{position:absolute}
.sans{font-family:"Poppins",Arial,sans-serif}
.photo{position:absolute}

/* top bar + nav */
.promo{left:0;top:0;width:1200px;height:31px;background:#cfcfcd;color:#fff;font:400 11px/31px "Poppins",sans-serif;text-align:center}
.nav{left:0;top:31px;width:1200px;height:94px;border-bottom:1px solid var(--line)}
.nav-links{left:89px;top:42px;display:flex;gap:14px;font:400 12px "Poppins",sans-serif;color:#6e6a68;letter-spacing:.3px}
.nav-links span.sep{color:#bbb}
.brand{left:500px;top:40px;width:200px;text-align:center;font:400 19px "Libre Baskerville",serif;color:#6e6a68;letter-spacing:.5px}
.nav-icons{left:794px;top:36px;display:flex;gap:20px}
.shop-btn{left:950px;top:59px;width:161px;height:45px;background:var(--blush);color:#fff;font:400 13px/45px "Libre Baskerville",serif;text-align:center}

/* hero */
.hero-center{left:361px;top:125px;width:477px;height:636px;background:var(--hero);text-align:center;color:#fff}
.hero-mark{margin-top:145px;font:400 22px "Libre Baskerville",serif;letter-spacing:3px}
.hero-title{margin-top:32px;font:400 43px/48px "Libre Baskerville",serif;letter-spacing:.5px}
.hero-copy{margin:30px auto 0;width:380px;font:400 12px/20px "Libre Baskerville",serif}
.hero-btns{margin-top:24px;display:flex;justify-content:center;gap:10px}
.btn-light{width:108px;height:38px;background:#fff;color:#8b8785;font:400 13px/38px "Libre Baskerville",serif}
.btn-ghost{width:157px;height:38px;border:1px solid #fff;color:#fff;font:400 13px/36px "Libre Baskerville",serif}

/* story */
.story{left:0;top:761px;width:1200px;height:626px;background:var(--shell)}
.story-title{left:400px;top:945px;width:400px;text-align:center;font:400 34px/42px "Libre Baskerville",serif;color:var(--heading)}
.story-copy{left:420px;top:1089px;width:360px;text-align:center;font:400 12px/21px "Libre Baskerville",serif;color:var(--muted)}

/* products */
.product-title{font:400 34px "Libre Baskerville",serif;letter-spacing:.5px}
.product-copy{font:400 12.5px/18px "Libre Baskerville",serif;width:240px}
.btn-dark{background:var(--ink);color:#fff;font:700 14px/49px "Libre Baskerville",serif;text-align:center}

/* values */
.section-title{left:0;width:1200px;text-align:center;font:400 46px "Libre Baskerville",serif;color:var(--heading)}
.section-sub{left:0;width:1200px;text-align:center;font:400 20px "Libre Baskerville",serif;color:var(--heading)}
.value{width:300px;text-align:center}
.value h3{font:400 17px "Libre Baskerville",serif;color:var(--heading);letter-spacing:.3px}
.value p{margin-top:16px;font:400 12px/20px "Libre Baskerville",serif;color:var(--muted);padding:0 20px}
.divider{left:83px;top:2580px;width:1034px;height:1px;background:var(--line)}

/* testimonial */
.quote-mark{left:700px;top:2640px;font:400 200px/1 "Libre Baskerville",serif;color:#f1ebe9}
.testi-title{left:610px;top:2741px;font:400 34px "Libre Baskerville",serif;color:var(--heading)}
.testi-copy{left:610px;top:2800px;width:490px;font:400 12.5px/22px "Libre Baskerville",serif;color:var(--muted)}
.stars{left:610px;top:2890px;color:var(--star);font-size:15px;letter-spacing:1px}
.testi-name{left:610px;top:2924px;font:400 15px "Libre Baskerville",serif;color:var(--blush)}
.dots{left:610px;top:2975px;display:flex;gap:8px}
.dots i{display:block;width:20px;height:2px;background:var(--line)}
.dots i.on{background:var(--blush)}

/* videos */
.caption{left:0;top:3652px;width:1200px;text-align:center;font:400 19px "Libre Baskerville",serif;color:var(--heading)}
.pager{top:3656px;font:400 14px "Libre Baskerville",serif;color:var(--heading)}

/* subscribe */
.sub-title{left:0;top:3765px;width:1200px;text-align:center;font:400 38px "Libre Baskerville",serif;color:var(--heading)}
.sub-copy{left:0;top:3823px;width:1200px;text-align:center;font:400 11px "Libre Baskerville",serif;color:var(--muted)}
.sub-field{left:214px;top:3864px;width:614px;height:49px;background:var(--field);font:400 12px/49px "Libre Baskerville",serif;color:#b3adab;padding-left:38px}
.sub-btn{left:828px;top:3864px;width:156px;height:49px;background:var(--blush);color:#fff;font:700 14px/49px "Libre Baskerville",serif;text-align:center}

/* footer */
.footer{left:0;top:4022px;width:1200px;height:432px;background:var(--footer);color:#fff}
.foot-brand{left:90px;top:4218px;width:282px;text-align:center;font:400 30px "Libre Baskerville",serif;letter-spacing:.5px}
.foot-col{top:4116px}
.foot-col h4{font:400 17px "Libre Baskerville",serif;margin-bottom:18px}
.foot-col li{list-style:none;font:400 13px/28px "Poppins",sans-serif}
.socials{left:869px;top:4178px;display:flex;gap:12px}
.socials span{display:block;width:45px;height:45px;border-radius:50%;background:rgba(255,255,255,.18)}
.foot-line{left:90px;top:4397px;width:1020px;height:1px;background:rgba(255,255,255,.55)}
.copyright{left:0;top:4418px;width:1200px;text-align:center;font:400 11px "Poppins",sans-serif;color:#fff}
.to-top{left:1128px;top:4374px;width:46px;height:46px;border-radius:50%;background:#fff}
</style>
</head>
<body>

<div class="abs promo">Enjoy 20% Off Your First Order. Shop Now!</div>

<header class="abs nav">
  <nav class="abs nav-links">
    <span>HOME</span><span class="sep">|</span><span>OUR STORY</span><span class="sep">|</span><span>SHOP</span><span class="sep">|</span><span>JOURNAL</span><span class="sep">|</span><span>CONTACT</span>
  </nav>
  <div class="abs brand">DEW HARBOR</div>
  <div class="abs nav-icons">
    <svg width="24" height="24" viewBox="0 0 24 24" fill="none" stroke="#6e6a68" stroke-width="1.6"><circle cx="10" cy="10" r="7"/><path d="M15 15l6 6"/></svg>
    <svg width="26" height="24" viewBox="0 0 26 24" fill="none" stroke="#6e6a68" stroke-width="1.6"><path d="M13 21S3 14.5 3 8.5A5 5 0 0 1 13 6a5 5 0 0 1 10 2.5C23 14.5 13 21 13 21z"/></svg>
    <svg width="28" height="24" viewBox="0 0 28 24" fill="none" stroke="#6e6a68" stroke-width="1.6"><path d="M2 3h4l3 12h13l3-9H8"/><circle cx="11" cy="20" r="1.5"/><circle cx="20" cy="20" r="1.5"/></svg>
  </div>
  <div class="abs shop-btn" style="top:28px">Shop the Collection</div>
</header>

<!-- hero -->
<div class="photo" role="img" aria-label="Serum dropper bottle on a stone plinth with dried berries in soft shadowed light" style="left:0;top:125px;width:361px;height:636px;background:linear-gradient(160deg,#e9e8e3 0%,#c9c6be 55%,#8c877d 100%)"></div>
<section class="abs hero-center">
  <div class="hero-mark">DEW HARBOR</div>
  <h1 class="hero-title">ELEVATED<br>SKIN WELLNESS,<br>NATURALLY</h1>
  <p class="hero-copy">Harness the power of botanical actives and organic innovation to bring your skin into perfect alignment.</p>
  <div class="hero-btns"><div class="btn-light">Shop Now</div><div class="btn-ghost">Discover Our Story</div></div>
</section>
<div class="photo" role="img" aria-label="Smiling woman with long wavy hair touching her cheek" style="left:838px;top:125px;width:362px;height:636px;background:linear-gradient(170deg,#e6dcd6 0%,#cdb3a3 50%,#a98772 100%)"></div>

<!-- story -->
<section class="abs story"></section>
<div class="photo" role="img" aria-label="Serum bottle beside its box on a pale grey background" style="left:71px;top:877px;width:304px;height:351px;border-radius:0 0 152px 152px;background:linear-gradient(180deg,#dcdcda,#cfcfcc)"></div>
<h2 class="abs story-title">ELEVATED<br>SKIN WELLNESS,<br>NATURALLY</h2>
<p class="abs story-copy">At Dew Harbor, we believe that beauty blooms through balance. Our formulations are crafted with purpose — blending potent botanicals with modern skin science to support your skin's rhythm, naturally.</p>
<div class="photo" role="img" aria-label="Woman in a towel turban applying skincare at a mirror" style="left:856px;top:839px;width:181px;height:219px;border-radius:90px 90px 0 0;background:linear-gradient(180deg,#6fa8b8 0%,#e8e2da 45%,#b89d87 100%)"></div>
<div class="photo" role="img" aria-label="Woman looking into a mirror in a bright room" style="left:838px;top:1162px;width:251px;height:131px;border-radius:0 60px 0 0;background:linear-gradient(90deg,#a89580,#6b5f4c 55%,#d8d2c6)"></div>

<!-- products -->
<div class="photo" role="img" aria-label="Golden serum bottle lying in shimmering water" style="left:0;top:1387px;width:600px;height:527px;background:linear-gradient(135deg,#f0d8b5 0%,#d9b07d 50%,#b98a57 100%)"></div>
<h3 class="abs product-title" style="left:76px;top:1498px;color:var(--ink)">LUMIVELT</h3>
<p class="abs product-copy" style="left:76px;top:1550px;color:var(--ink)">Lightweight hydration that refines, balances, and leaves skin luminous.</p>
<div class="abs btn-dark" style="left:358px;top:1738px;width:155px;height:48px" aria-label="View Details"></div>

<div class="photo" role="img" aria-label="White serum bottle resting on a driftwood branch against a mauve backdrop" style="left:600px;top:1387px;width:600px;height:527px;background:linear-gradient(160deg,#d3bbb3 0%,#c1a79c 55%,#7a5d4c 100%)"></div>
<h3 class="abs product-title" style="left:667px;top:1503px;color:#fff">SERAPOISE</h3>
<p class="abs product-copy" style="left:667px;top:1563px;color:#fff;width:230px">A restorative cream that deeply nourishes while keeping skin's natural rhythm in harmony.</p>
<div class="abs btn-dark" style="left:667px;top:1651px;width:156px;height:49px">View Details</div>

<!-- values -->
<h2 class="abs section-title" style="top:1982px">GROUNDED IN NATURE</h2>
<p class="abs section-sub" style="top:2043px">BACKED BY SCIENCE</p>
<div class="photo" role="img" aria-label="Oil dropper bottle with stones and seeds" style="left:150px;top:2101px;width:284px;height:283px;background:linear-gradient(160deg,#eeeeea,#c9c2b4 60%,#7d705c)"></div>
<div class="photo" role="img" aria-label="Amber bottles with soap and pampas grass on a warm backdrop" style="left:458px;top:2101px;width:284px;height:283px;background:linear-gradient(160deg,#d9b69a,#a57a5a 60%,#5d4532)"></div>
<div class="photo" role="img" aria-label="Two women in white applying skincare beside plants" style="left:764px;top:2101px;width:284px;height:283px;background:linear-gradient(160deg,#f1efeb,#d7d0c6 60%,#8b9a7a)"></div>
<div class="abs value" style="left:142px;top:2412px"><h3>BOTANICAL INGREDIENTS</h3><p>We source high-quality, plant-powered ingredients that are gentle, rooted in traditional healing practices.</p></div>
<div class="abs value" style="left:450px;top:2412px"><h3>HOLISTIC FORMULATIONS</h3><p>Each product is thoughtfully blended to support skin health from all angles - balancing function, feel, and long-term results.</p></div>
<div class="abs value" style="left:756px;top:2412px"><h3>SUSTAINABLE PRACTICES</h3><p>From packaging to production, we prioritize practices that are kind to the earth and respectful of your skin.</p></div>
<div class="abs divider"></div>

<!-- testimonial -->
<div class="abs" style="left:470px;top:2918px;width:84px;height:42px;border-radius:42px 42px 0 0;background:var(--blush-soft)"></div>
<div class="photo" role="img" aria-label="Smiling woman in a towel turban using a cotton pad" style="left:187px;top:2663px;width:346px;height:346px;border-radius:50%;background:radial-gradient(circle at 50% 45%,#e8d3c4,#c8ab98 60%,#d9d7d4);box-shadow:0 20px 40px rgba(0,0,0,.08)"></div>
<div class="abs quote-mark">“</div>
<h2 class="abs testi-title">WHAT OUR CLIENT SAY</h2>
<p class="abs testi-copy">After using Lumivelt for just a week, my skin looks noticeably brighter and more even. It feels like a reset for my face. My skin has always been sensitive, but Serapoise calmed the redness without feeling heavy.</p>
<div class="abs stars">★★★★★</div>
<div class="abs testi-name">MARISOL T SENSITIVE SKIN</div>
<div class="abs dots"><i></i><i class="on"></i><i></i></div>

<!-- videos -->
<h2 class="abs section-title" style="top:3094px;font-size:36px">RECENT VIDEOS</h2>
<div class="photo" role="img" aria-label="Woman in a white robe and towel turban" style="left:0;top:3157px;width:258px;height:465px;background:linear-gradient(160deg,#f2f0ee,#e2d2c6 60%,#cfc6c1)"></div>
<div class="photo" role="img" aria-label="Woman with a floral crown resting by the sea" style="left:268px;top:3157px;width:664px;height:465px;background:linear-gradient(180deg,#d5dbe0 0%,#b6c2ca 45%,#c8a892 75%,#a9856d 100%)"></div>
<svg class="abs" style="left:548px;top:3337px" width="104" height="104" viewBox="0 0 104 104"><circle cx="52" cy="52" r="52" fill="rgba(255,255,255,.45)"/><path d="M44 36l26 16-26 16z" fill="#fff"/></svg>
<div class="photo" role="img" aria-label="Woman holding a serum bottle near a ladder shelf" style="left:942px;top:3157px;width:258px;height:465px;background:linear-gradient(160deg,#efe6dc,#d8c6b4 60%,#6f6a4e)"></div>
<div class="abs pager" style="left:99px">← PREV</div>
<div class="abs caption">THE POWER OF BOTANICAL ACTIVES</div>
<div class="abs pager" style="left:1040px">NEXT →</div>

<!-- subscribe -->
<h2 class="abs sub-title">SUBSCRIBE &amp; GET 45% DISCOUNT</h2>
<p class="abs sub-copy">Become a Member and Unlock Exclusive Access to Our Best-Selling Products at an Unbeatable 45% Discount!</p>
<div class="abs sub-field">Enter your email</div>
<div class="abs sub-btn">Submit</div>

<!-- footer -->
<footer class="abs footer"></footer>
<div class="abs foot-brand">DEW HARBOR</div>
<div class="abs foot-col" style="left:436px"><h4>QUICK LINKS</h4><ul><li>› Home</li><li>› Our Story</li><li>› Shop</li><li>› Journal</li><li>› Contact</li></ul></div>
<div class="abs foot-col" style="left:650px"><h4>INFORMATION</h4><ul><li>› Search</li><li>› About Us</li><li>› Delivery Information</li><li>› Returns &amp; Refunds</li><li>› FAQ</li><li>› Contact Us</li></ul></div>
<div class="abs socials"><span aria-label="Social link"></span><span aria-label="Social link"></span><span aria-label="Social link"></span><span aria-label="Social link"></span></div>
<div class="abs foot-line"></div>
<div class="abs copyright">© Copyright 2025. All Rights Reserved</div>
<div class="abs to-top"><svg width="46" height="46" viewBox="0 0 46 46" fill="none" stroke="#8b8785" stroke-width="1.5"><path d="M23 30V16M17 22l6-6 6 6"/></svg></div>

</body>
</html>
```